Business Cards for a small business advisory (business services)

Professional look. Same as would apply for a lawyer, accountant, or other financial services professional. Please use the logo colors

Target Market(s)

small business owners

Industry/Entity Type

Financial Servics

Contact Information for Business Card

Name: Gavin L. Whitmore, CAIA / Title: Business Advisor / Office #: (718) 294-7716 / Mobile #: (917) 382-5047 / Email: g.whitmore@clearfieldventurepartners.example / Web: www.clearfieldventurepartners.example

Font styles to use
Sans Serif

```html
<!DOCTYPE html>
<html lang="en">
<head>
<meta charset="utf-8">
<title>Clearfield Venture Partners – Business Cards</title>
<link rel="stylesheet" href="https://fonts.googleapis.com/css2?family=Montserrat:wght@700&family=Poppins:wght@400;500&display=swap">
<style>
  :root {
    --navy: #1c3a6b;
    --green: #8cc63f;
    --ink: #2e2e2e;
    --paper: #ffffff;
    --backdrop: #9a9a9a;
    --rule: #6b7a99;
  }
  * { box-sizing: border-box; margin: 0; padding: 0; }
  html, body { width: 1093px; height: 1200px; overflow: hidden; }
  body { background: var(--backdrop); position: relative; font-family: "Poppins", sans-serif; }

  .card { position: absolute; left: 265px; width: 580px; height: 357px; }
  .card--front { top: 226px; background: var(--paper); }
  .card--back { top: 620px; background: var(--navy); }

  .brand { position: absolute; display: flex; align-items: center; gap: 12px; white-space: nowrap; }
  .brand__mark { width: 34px; height: 34px; border-radius: 50%; flex: none; background: var(--green); }
  .brand__name {
    font-family: "Montserrat", sans-serif; font-weight: 700;
    font-size: 28px; letter-spacing: 0.3px; line-height: 1.1;
  }

  .card--front .brand { left: 18px; top: 52px; }
  .card--front .brand__name { color: var(--navy); }

  .card--back .brand { left: 50%; top: 50%; transform: translate(-50%, -50%); }
  .card--back .brand__name { color: var(--green); }

  .holder { position: absolute; right: 30px; top: 180px; text-align: right; white-space: nowrap; }
  .holder__name {
    font-family: "Montserrat", sans-serif; font-weight: 700;
    font-size: 22px; color: var(--navy); text-transform: uppercase; line-height: 1.1;
  }
  .holder__cred { color: var(--green); }
  .holder__title { font-size: 17px; color: var(--ink); line-height: 1.25; }

  .accent-bar { position: absolute; right: 0; top: 183px; width: 16px; height: 43px; background: var(--green); }
  .divider { position: absolute; left: 0; top: 217px; width: 395px; height: 1px; background: var(--rule); }

  .contacts { position: absolute; left: 27px; top: 235px; list-style: none; }
  .contacts li { display: flex; align-items: center; gap: 8px; height: 24px; font-size: 17px; color: var(--ink); white-space: nowrap; }
  .contacts svg { width: 15px; height: 15px; flex: none; fill: var(--navy); }
</style>
</head>
<body>
  <section class="card card--front">
    <div class="brand">
      <span class="brand__mark"></span>
      <span class="brand__name">Clearfield Venture Partners</span>
    </div>

    <div class="holder">
      <p class="holder__name">Gavin L. Whitmore, <span class="holder__cred">CAIA</span></p>
      <p class="holder__title">Business Advisor</p>
    </div>
    <div class="accent-bar"></div>
    <div class="divider"></div>

    <ul class="contacts">
      <li>
        <svg viewBox="0 0 24 24"><path d="M6.6 10.8a15.1 15.1 0 0 0 6.6 6.6l2.2-2.2a1 1 0 0 1 1-.25 11.4 11.4 0 0 0 3.6.57 1 1 0 0 1 1 1V20a1 1 0 0 1-1 1A17 17 0 0 1 3 4a1 1 0 0 1 1-1h3.5a1 1 0 0 1 1 1c0 1.25.2 2.45.57 3.57a1 1 0 0 1-.25 1z"/></svg>
        (718) 294-7716
      </li>
      <li>
        <svg viewBox="0 0 24 24"><path d="M7 1h10a2 2 0 0 1 2 2v18a2 2 0 0 1-2 2H7a2 2 0 0 1-2-2V3a2 2 0 0 1 2-2zm0 3v14h10V4zm5 15.5a1 1 0 1 0 0 2 1 1 0 0 0 0-2z"/></svg>
        (917) 382-5047
      </li>
      <li>
        <svg viewBox="0 0 24 24"><path d="M2 5h20v14H2zm2 2v.5l8 5 8-5V7zm0 2.8V17h16V9.8l-8 5z"/></svg>
        g.whitmore@clearfieldventurepartners.example
      </li>
      <li>
        <svg viewBox="0 0 24 24"><path d="M12 2a10 10 0 1 0 0 20 10 10 0 0 0 0-20zm6.9 9h-3a15 15 0 0 0-1.3-6A8 8 0 0 1 18.9 11zM12 4c.9 1.3 1.8 3.8 1.9 7h-3.8c.1-3.2 1-5.7 1.9-7zM9.4 5A15 15 0 0 0 8.1 11h-3a8 8 0 0 1 4.3-6zM5.1 13h3a15 15 0 0 0 1.3 6 8 8 0 0 1-4.3-6zM12 20c-.9-1.3-1.8-3.8-1.9-7h3.8c-.1 3.2-1 5.7-1.9 7zm2.6-1a15 15 0 0 0 1.3-6h3a8 8 0 0 1-4.3 6z"/></svg>
        www.clearfieldventurepartners.example
      </li>
    </ul>
  </section>

  <section class="card card--back">
    <div class="brand">
      <span class="brand__mark"></span>
      <span class="brand__name">Clearfield Venture Partners</span>
    </div>
  </section>
</body>
</html>
```